Lending Harbor Partners - business cards

we need new business cards for my company.
i've been in business for 25 years.
my wife and I are mortgage brokers.

we just bought the domain for a website with www.bluekeyhomes.example
that could be used in the design also.

On the business card would be
Front card:

Dale Whitcombe
Owner/Loan Officer
Cell: (555) 814-2976
Lending Harbor Partners
4237 Maple Crest Lane
Santa Clarita, CA 90000
Office (555) 430-7152
Fax (555) 430-7159
website www.bluekeyhomes.example

Back of Card:

LHP BRE #0873512 NMLS #528946
Dale Whitcombe BRE # 06739481 NMLS #527314

```html
<!DOCTYPE html>
<html lang="en">
<head>
<meta charset="utf-8">
<title>Lending Harbor Partners – Business Cards</title>
<link rel="stylesheet" href="https://fonts.googleapis.com/css2?family=Open+Sans:wght@400;600;700;800&display=swap">
<style>
  :root {
    --backdrop: #e9e9e9;
    --card: #ffffff;
    --brand-orange: #e2642a;
    --brand-grey: #8e8e8e;
    --ink: #222222;
    --ink-soft: #444444;
  }
  * { box-sizing: border-box; margin: 0; padding: 0; }
  html, body {
    width: 1200px;
    height: 1000px;
    overflow: hidden;
    background: var(--backdrop);
    font-family: "Open Sans", Arial, sans-serif;
  }
  .sheet { position: relative; width: 1200px; height: 1000px; }
  .card {
    position: absolute;
    width: 760px;
    height: 440px;
    background: var(--card);
    box-shadow: 0 2px 10px rgba(0,0,0,0.12);
  }
  .card--back { left: 400px; top: 40px; }
  .card--front { left: 40px; top: 520px; }

  .brand { position: absolute; display: flex; align-items: center; }
  .brand__mark { background: var(--brand-orange); flex: none; }
  .brand__name {
    color: var(--brand-grey);
    font-weight: 800;
    text-transform: uppercase;
    line-height: 0.95;
    letter-spacing: 0.01em;
  }
  .card--back .brand { left: 36px; top: 30px; gap: 10px; }
  .card--back .brand__mark { width: 44px; height: 44px; }
  .card--back .brand__name { font-size: 14px; }
  .card--front .brand { left: 44px; top: 40px; gap: 18px; }
  .card--front .brand__mark { width: 120px; height: 120px; }
  .card--front .brand__name { font-size: 38px; }

  .licenses {
    position: absolute;
    right: 40px;
    bottom: 40px;
    text-align: right;
    font-size: 21px;
    line-height: 1.35;
    color: var(--ink);
    letter-spacing: 0.02em;
  }

  .person { position: absolute; right: 40px; top: 200px; text-align: right; }
  .person__name { color: var(--brand-orange); font-weight: 700; font-size: 28px; line-height: 1.1; }
  .person__title { color: var(--ink); font-size: 24px; line-height: 1.2; }

  .contact {
    position: absolute;
    right: 40px;
    bottom: 36px;
    text-align: right;
    color: var(--ink-soft);
    font-size: 19px;
    line-height: 1.6;
  }
  .contact__label { font-weight: 700; color: var(--ink); }
  .contact__label--cell { color: var(--ink-soft); font-style: italic; }
  .contact__sep { color: var(--brand-orange); font-weight: 700; padding: 0 2px; }
  .contact__web { color: var(--brand-orange); font-weight: 700; font-size: 22px; }
</style>
</head>
<body>
<main class="sheet">
  <section class="card card--back" aria-label="Card back">
    <div class="brand">
      <span class="brand__mark"></span>
      <span class="brand__name">Lending<br>Harbor<br>Partners</span>
    </div>
    <p class="licenses">
      LHP BRE #0873512 NMLS #528946<br>
      Dale Whitcombe BRE # 06739481 NMLS #527314
    </p>
  </section>

  <section class="card card--front" aria-label="Card front">
    <div class="brand">
      <span class="brand__mark"></span>
      <span class="brand__name">Lending<br>Harbor<br>Partners</span>
    </div>
    <div class="person">
      <p class="person__name">Dale Whitcombe</p>
      <p class="person__title">Owner/Loan Officer</p>
    </div>
    <div class="contact">
      <p>4237 Maple Crest Lane, Santa Clarita, CA 90000</p>
      <p><span class="contact__label contact__label--cell">Cell:</span> (555) 814-2976 <span class="contact__sep">|</span> <span class="contact__label">Office</span> (555) 430-7152 <span class="contact__sep">|</span> <span class="contact__label">Fax</span> (555) 430-7159</p>
      <p class="contact__web">www.bluekeyhomes.example</p>
    </div>
  </section>
</main>
</body>
</html>
```